Cosmetic Surgery Practice Advertising brochures

Our practice needs a brochure containing general information and procedures we offer for advertising and marketing purposes.

Our website is currently being revamped but older version is available www.verandaaesthetic.example

Our one of a kind Cosmetic Surgery Practice is second to none in southern Louisiana. Clients come to our practice from all over the country in seek of our top notch care where we seek to find a beauty that is unique to you! Everyone who walks through the doors is treated as an A list celebrity from the complementary consultation, to the walk-in walk-out surgery that is performed here in our facility under Local anesthesia. That is some of the key differences here at Rosewick:

In facility procedures = one up front all inclusive pricing. Consultations are complementary and you will meet with the Doctor himself.
No general sedation, rather local and deep sedation= walk out afterwards.
Quality of care is incomparable, patients given our cell phone numbers.

We offer Breast Augmentations, Tummy Tucks, Face procedures including neck, face, eyelid, brow lifts, etc, breast augmentations both implants and lift/reduction and liposuction with & without fat transfers to buttock or cheecks.

Most Cosmetic Surgeons typically have a specialty based practice from which they build from, like a Dermatology or ENT practice. Because our surgeon is a General Surgeon, he does not have a routine relationship client base, and must attract new patients organically. Other physicians that do not offer Cosmetic surgery services to relevantly related client base, therefore need to refer out to a surgeon that does.

Target Market(s)

Women interested in anesthetics, beauty, looking to feel their best

Industry/Entity Type

Cosmetic

Font styles to use
Serif
Script

Requirements
Must have
• Doctor Bio, Map, logo
Nice to have
• Beautiful women, CREATIVITY and ORIGINALITY
Should not have
• Harsh lines

```html
<!DOCTYPE html>
<html lang="en">
<head>
<meta charset="utf-8">
<title>Rosewick Brochure</title>
<link href="https://fonts.googleapis.com/css2?family=Montserrat:wght@500;700;800&family=Open+Sans:wght@400;600&family=Roboto+Condensed:wght@700&display=swap" rel="stylesheet">
<style>
:root{
  --bg:#3a3a3a;
  --orange:#b8732e;
  --ink:#1c1a19;
  --text:#3b3b3b;
  --paper:#ffffff;
}
*{box-sizing:border-box;margin:0;padding:0}
html,body{width:1200px;height:1200px;overflow:hidden;background:var(--bg)}
body{font-family:"Open Sans",sans-serif;color:var(--text);position:relative}
.spread{position:absolute;left:220px;width:760px;height:588px;display:flex;box-shadow:0 6px 18px rgba(0,0,0,.4)}
.spread--outside{top:8px}
.spread--inside{top:604px}
.panel{width:253.33px;height:100%;position:relative;overflow:hidden}
.panel--white{background:var(--paper)}
.panel--orange{background:var(--orange);color:#fff}
h2.doc-name{font-family:Montserrat,sans-serif;font-weight:800;color:var(--orange);font-size:15px;margin:26px 0 8px 20px}
.bio{padding:0 18px 0 20px;font-size:7.3px;line-height:1.45}
.bio p{margin-bottom:8px;text-align:justify}
.doc-portrait{float:right;width:88px;height:104px;margin:0 0 6px 8px;background:linear-gradient(160deg,#d8d4cf,#8d6e5c)}
h3.section{font-family:Montserrat,sans-serif;font-weight:700;color:var(--orange);font-size:11px;margin:4px 0 5px 20px}
.cert-list{list-style:none;padding:0 16px 0 20px;font-size:7.6px;font-weight:600;line-height:1.4}
.cert-list li{display:flex;gap:5px;margin-bottom:3px}
.tick{flex:none;width:9px;height:9px;margin-top:1px}
.artist{font-size:7.8px;font-weight:600;margin:10px 20px 0}
.artist a{color:var(--orange);text-decoration:none}
.hero-photo{height:150px;background:linear-gradient(180deg,#d8a56e,#b8732e)}
.map-card{position:absolute;top:128px;left:24px;width:205px;height:122px;border-radius:10px;background:#fff;padding:6px;box-shadow:0 3px 8px rgba(0,0,0,.25)}
.map{width:100%;height:100%;border-radius:6px;background:linear-gradient(135deg,#eef0f2,#dfe3e7)}
.brand{display:flex;align-items:center;gap:6px;font-family:Montserrat,sans-serif;font-weight:700}
.brand-dot{width:14px;height:14px;border-radius:50%;background:currentColor}
.brand--contact{position:absolute;top:272px;left:28px;font-size:22px;color:#fff}
.contact{position:absolute;top:330px;left:26px;right:18px;font-size:7.6px;line-height:1.45}
.contact h4{font-family:Montserrat,sans-serif;font-weight:700;font-size:10px;margin-bottom:6px}
.contact-row{display:flex;gap:6px;margin-bottom:4px}
.contact-row svg{flex:none;width:10px;height:10px;margin-top:1px}
.contact-note{font-weight:600;margin-top:8px}
.cover-top{height:250px;background:#fff}
.brand--cover{position:absolute;top:22px;left:46px;font-size:28px;color:var(--ink)}
.brand--cover .brand-dot{background:var(--orange)}
.brand-sub{position:absolute;top:56px;left:70px;font-size:8px;color:var(--ink);font-family:Montserrat,sans-serif;font-weight:500}
.cover-black{position:absolute;top:250px;left:0;right:0;bottom:0;background:var(--ink)}
.cover-ring{position:absolute;top:80px;left:32px;width:208px;height:208px;border-radius:50%;border:5px solid var(--orange);box-shadow:0 0 0 4px #fff,0 0 0 6px var(--ink);background:linear-gradient(150deg,#dfe3ee,#cdb39a)}
.cover-title{position:absolute;top:372px;left:0;right:0;text-align:center;font-family:"Roboto Condensed",sans-serif;font-weight:700;font-size:20px;line-height:1.15;color:#fff}
.cover-title .accent{color:var(--orange)}
.cover-url{position:absolute;top:470px;left:0;right:0;text-align:center;font-size:8.5px;color:#fff;font-weight:600}
h3.center-title{font-family:Montserrat,sans-serif;font-weight:800;color:var(--orange);font-size:10.5px;margin:24px 18px 8px;line-height:1.2}
.about{padding:0 18px;font-size:7.3px;line-height:1.5;text-align:justify}
.about p{margin-bottom:8px}
.about p.wrap{padding-right:70px}
.doc-standing{position:absolute;right:0;bottom:0;width:120px;height:215px;background:linear-gradient(180deg,#c9c6c2,#6d6b6a)}
.badge{position:absolute;left:40px;width:38px;height:38px;border-radius:50%;border:2px solid #9aa6b8;background:#eef1f5}
.ba-head{padding:20px 16px 4px}
.ba-head h3{font-family:Montserrat,sans-serif;font-weight:800;font-size:10.5px;margin-bottom:4px}
.ba-head p{font-size:7px;line-height:1.4}
.proc{padding:0 14px;margin-top:7px}
.proc h5{font-family:Montserrat,sans-serif;font-weight:700;font-size:7.8px;margin-bottom:3px;text-transform:uppercase}
.panel--white .proc h5{color:var(--orange)}
.spacer{height:12px}
.pair{display:flex;gap:6px}
.shot{position:relative;flex:1;height:62px;border-radius:5px;border:1px solid #222;overflow:hidden}
.shot span{position:absolute;left:0;bottom:0;background:var(--ink);color:#fff;font-size:6.5px;font-weight:600;padding:2px 7px;border-top-right-radius:5px}
.shot--skin{background:linear-gradient(135deg,#e2c1a3,#a9785a)}
.shot--face{background:linear-gradient(135deg,#8a6a55,#2c2420)}
.quotes{padding:10px 16px 0}
.quote{border:1.2px solid var(--orange);border-radius:8px;padding:6px 8px;font-size:6.8px;line-height:1.4;margin-bottom:7px;position:relative}
.quote b{display:block;text-align:right;font-weight:600;margin-top:2px}
.quote::before{content:"\201C";position:absolute;left:-4px;top:-8px;background:#fff;color:var(--orange);font-size:16px;font-family:Montserrat,sans-serif;font-weight:800;line-height:1}
</style>
</head>
<body>

<section class="spread spread--outside">
  <div class="panel panel--white">
    <h2 class="doc-name">Arun Velamuri, MD, FGSA</h2>
    <div class="bio">
      <div class="doc-portrait" role="img" aria-label="Portrait of the surgeon in a white coat"></div>
      <p>Our Surgeon, Dr. Arun Velamuri, MD, FGSA, is Board Certified in General Surgery, and also is a Diplomate of the Gulf Board of Aesthetic Surgery, practicing General Surgery in the South for over 30 years, &amp; Cosmetic Surgery for over 15 years.</p>
      <p>Most people know Dr. Arun Velamuri simply as “Dr. Arun”. He is married to Dr. Lakshmi Raman, a Radiologist also in practice for many years. He has two children, daughter Priya Devi, now teaching music in Riverbend, and a son Kiran Raman, an architect who is currently living in Portugal.</p>
      <p>Dr. Arun is trained extensively in several areas of Cosmetic Surgery. Over the years, Dr. Arun has acquired excellent skills from hands-on training with experts in the fields of Liposuction, Tummy Tuck (Abdominoplasty), Breast Augmentation, Breast Reduction, and Facial Cosmetic Procedures.</p>
    </div>
    <h3 class="section">Certifications:</h3>
    <ul class="cert-list">
      <li><svg class="tick" viewBox="0 0 10 10"><circle cx="5" cy="5" r="5" fill="#b8732e"/><path d="M2.8 5.2l1.5 1.5 3-3" stroke="#fff" stroke-width="1.3" fill="none"/></svg>Board Certified General Surgeon</li>
      <li><svg class="tick" viewBox="0 0 10 10"><circle cx="5" cy="5" r="5" fill="#b8732e"/><path d="M2.8 5.2l1.5 1.5 3-3" stroke="#fff" stroke-width="1.3" fill="none"/></svg>Diplomate of the Gulf Board of Aesthetic Surgery</li>
      <li><svg class="tick" viewBox="0 0 10 10"><circle cx="5" cy="5" r="5" fill="#b8732e"/><path d="M2.8 5.2l1.5 1.5 3-3" stroke="#fff" stroke-width="1.3" fill="none"/></svg>Fellow of the Gulf Surgical Academy</li>
      <li><svg class="tick" viewBox="0 0 10 10"><circle cx="5" cy="5" r="5" fill="#b8732e"/><path d="M2.8 5.2l1.5 1.5 3-3" stroke="#fff" stroke-width="1.3" fill="none"/></svg>Fellow of Coastal Academy of Aesthetic Medicine</li>
      <li><svg class="tick" viewBox="0 0 10 10"><circle cx="5" cy="5" r="5" fill="#b8732e"/><path d="M2.8 5.2l1.5 1.5 3-3" stroke="#fff" stroke-width="1.3" fill="none"/></svg>Member of Southern Society of Contour Surgery</li>
      <li><svg class="tick" viewBox="0 0 10 10"><circle cx="5" cy="5" r="5" fill="#b8732e"/><path d="M2.8 5.2l1.5 1.5 3-3" stroke="#fff" stroke-width="1.3" fill="none"/></svg>General surgical practice over 30 years</li>
      <li><svg class="tick" viewBox="0 0 10 10"><circle cx="5" cy="5" r="5" fill="#b8732e"/><path d="M2.8 5.2l1.5 1.5 3-3" stroke="#fff" stroke-width="1.3" fill="none"/></svg>Cosmetic surgical practice over 15 years</li>
    </ul>
    <p class="artist">Self-taught artist</p>
    <p class="artist">Gallery at <a>www.velamuriart.example</a></p>
  </div>

  <div class="panel panel--orange">
    <div class="hero-photo" role="img" aria-label="Smiling woman with long wavy hair, warm orange toned photo"></div>
    <div class="map-card"><div class="map" role="img" aria-label="Street map showing the location of the practice"></div></div>
    <div class="brand brand--contact"><span class="brand-dot"></span>Rosewick</div>
    <div class="contact">
      <h4>CONTACT US</h4>
      <div class="contact-row"><svg viewBox="0 0 10 10"><path d="M5 0.5a3.2 3.2 0 0 0-3.2 3.2C1.8 6.2 5 9.5 5 9.5s3.2-3.3 3.2-5.8A3.2 3.2 0 0 0 5 .5z" fill="#fff"/><circle cx="5" cy="3.7" r="1.2" fill="#b8732e"/></svg><span><b>Rosewick Center for Cosmetic Surgery</b><br>210 Magnolia Crest Blvd Building C,<br>Suite 4 Bayou Crest, LA 70500</span></div>
      <div class="contact-row"><svg viewBox="0 0 10 10"><path d="M2.2 .8l1.6 1.9-.9 1.2c.6 1.3 1.6 2.3 2.9 2.9l1.2-.9 1.9 1.6-.9 1.5C4.8 9 1 5.2.7 1.7z" fill="#fff"/></svg><span>(555) 014-2290</span></div>
      <div class="contact-row"><svg viewBox="0 0 10 10"><rect x=".5" y="2" width="9" height="6.2" rx="1" fill="#fff"/><path d="M.8 2.4L5 5.6l4.2-3.2" stroke="#b8732e" stroke-width=".9" fill="none"/></svg><span>info@verandaaesthetic.example</span></div>
      <div class="contact-row"><svg viewBox="0 0 10 10"><circle cx="5" cy="5" r="4.3" stroke="#fff" stroke-width="1" fill="none"/><path d="M.8 5h8.4M5 .7c-2 2.6-2 6 0 8.6M5 .7c2 2.6 2 6 0 8.6" stroke="#fff" stroke-width=".8" fill="none"/></svg><span>www.verandaaesthetic.example</span></div>
      <p class="contact-note">Complimentary Consultations<br>CarePlus payment plans accepted</p>
    </div>
  </div>

  <div class="panel panel--white">
    <div class="cover-top"></div>
    <div class="brand brand--cover"><span class="brand-dot"></span>Rosewick</div>
    <div class="brand-sub">Center for Cosmetic Surgery</div>
    <div class="cover-black"></div>
    <div class="cover-ring" role="img" aria-label="Woman's face being examined by gloved hands"></div>
    <h1 class="cover-title"><span class="accent">WELCOME TO</span><br>ROSEWICK CENTER FOR<br><span class="accent">COSMETIC SURGERY</span></h1>
    <p class="cover-url">www.verandaaesthetic.example</p>
  </div>
</section>

<section class="spread spread--inside">
  <div class="panel panel--white">
    <h3 class="center-title">BAYOU CREST'S COSMETIC SURGERY<br>CENTER</h3>
    <div class="about">
      <p>Rosewick is a free-standing facility that offers the latest in Cosmetic Surgery. Our Board Certified Surgeon, Dr. Arun Velamuri M.D. founded Rosewick in 2011 but has been practicing for over thirty years.</p>
      <p>Complimentary consultations are available for patients who want to learn more about cosmetic surgery procedures, such as having a tummy tuck, liposuction, breast augmentation, butt lifts, facelifts, or any other cosmetic related concern. During this visit, you will meet with the doctor himself, not a consultant.</p>
      <p class="wrap">Rosewick's reputation for a quality of service that is second to none comes from the relationships established with our satisfied clients! Whether your cosmetic goals are simply for a boost of confidence, or you are looking to restore a more youthful version of yourself, Rosewick Center for Cosmetic Surgery has the expertise to help you achieve a sense of beauty that is unique to you!</p>
    </div>
    <div class="badge" style="top:430px" role="img" aria-label="Professional membership badge"></div>
    <div class="badge" style="top:482px" role="img" aria-label="Professional membership badge"></div>
    <div class="badge" style="top:534px" role="img" aria-label="Professional membership badge"></div>
    <div class="doc-standing" role="img" aria-label="Standing portrait of the surgeon in a grey suit"></div>
  </div>

  <div class="panel panel--orange">
    <div class="ba-head">
      <h3>WELCOME TO OUR BEFORE &amp; AFTERS</h3>
      <p>Please scroll down to find the procedure you're most interested in or visit the procedure page from our menu to see before &amp; after pictures, too. Viewer discretion is advised.</p>
    </div>
    <div class="proc"><h5>Brazilian Butt Lift</h5><div class="pair"><div class="shot shot--skin" role="img" aria-label="Before photo"><span>Before</span></div><div class="shot shot--skin" role="img" aria-label="After photo"><span>After</span></div></div></div>
    <div class="proc"><h5>Cosmetic Breast Surgery</h5><div class="pair"><div class="shot shot--skin" role="img" aria-label="Before photo"><span>Before</span></div><div class="shot shot--skin" role="img" aria-label="After photo"><span>After</span></div></div></div>
    <div class="proc"><h5>Face Lift Surgery</h5><div class="pair"><div class="shot shot--face" role="img" aria-label="Before photo"><span>Before</span></div><div class="shot shot--face" role="img" aria-label="After photo"><span>After</span></div></div></div>
    <div class="proc"><h5>Brow Lift Surgery</h5><div class="pair"><div class="shot shot--face" role="img" aria-label="Before photo"><span>Before</span></div><div class="shot shot--face" role="img" aria-label="After photo"><span>After</span></div></div></div>
    <div class="proc"><h5>Eyelid Surgery</h5><div class="pair"><div class="shot shot--face" role="img" aria-label="Before photo"><span>Before</span></div><div class="shot shot--face" role="img" aria-label="After photo"><span>After</span></div></div></div>
  </div>

  <div class="panel panel--white">
    <div class="spacer"></div>
    <div class="proc"><h5>Liposuction</h5><div class="pair"><div class="shot shot--skin" role="img" aria-label="Before photo"><span>Before</span></div><div class="shot shot--skin" role="img" aria-label="After photo"><span>After</span></div></div></div>
    <div class="proc"><h5>Lip Augmentation</h5><div class="pair"><div class="shot shot--skin" role="img" aria-label="Before photo"><span>Before</span></div><div class="shot shot--face" role="img" aria-label="After photo"><span>After</span></div></div></div>
    <div class="proc"><h5>Male Cosmetic Surgery</h5><div class="pair"><div class="shot shot--skin" role="img" aria-label="Before photo"><span>Before</span></div><div class="shot shot--skin" role="img" aria-label="After photo"><span>After</span></div></div></div>
    <div class="proc"><h5>Tummy Tuck Surgery (Abdominoplasty)</h5><div class="pair"><div class="shot shot--skin" role="img" aria-label="Before photo"><span>Before</span></div><div class="shot shot--skin" role="img" aria-label="After photo"><span>After</span></div></div></div>
    <div class="quotes">
      <div class="quote">I just want to say thank you for being so helpful before and after my surgery. You guys made me feel at ease, and that meant a lot.<b>– L. Marren</b></div>
      <div class="quote">Dana is very nice and easy to work with. Everyone including Dr. Arun is very nice and informative. I would highly recommend your services to anyone I know.<b>– Talia R.</b></div>
      <div class="quote">I love the staff and how they approach you and talk to you as a person, not a paycheck. I would def recommend to friends and family to go here.<b>– Monica S.</b></div>
    </div>
  </div>
</section>

</body>
</html>
```